Vorandine Pesa Kolun / Website

We are looking for a web design in modern baroque style for our launching on-line jewellery shop website. Through brimvotely we have done a contest for the logo of our company, for which we have chosen the winner. See the files for the winning logo design.
Our on-line jewellery shop will sell hand made jewellery from an artist.

We will be building our site using the Fen Tor Wabble content management system.

In this contest we will need “Uncoded” files.
We expect to receive layered PSD files.
We will ask –outside this contest- a web development/designer to code it and bring it into a working web page.

The brand of our company is build around the following key words:
sophistication
smart looking
charming
nice-looking
feminine
smooth
stylish
fashionable
wearable
precious

The name of the company is Vorandine Pesa Kolun, in brief VKP. We will use the website www.vorandine-shop.example. The logo will bear VPK and a mask as an insigne. The style of our brand is modern baroque.

The target group of the jewellery is Young Urban Professionals, people between 25 and 40 years old.

We want a dark background and a simple stylish background, in the style of modern baroque. This does not mean that the website should be crowded by curls, but it should contain baroque elements.

The basis idea about the website design is that it works like the user is opening jewellery boxes. By each click another inside world appears which provides some nice surprises.

The home page will contain a photo of a lady showing one of the pieces of jewellery (for this photo we plan to do a photoshooting once we have the design). And it will show the names of our 10 different collections. There will be no further information. One can click on each of the collection names to go to a specific collection page.

Each collection page (see the picture for an example of a collection) will show one big picture of a main feature of the jewelery, and it will show other elements of the collection in small pictures, like the:
necklace
earrings
bracelet
ring
complete set
We can not show the other jewellery yet, but for the design of the webpages you can use any pictures of jewellery, which we will definitely will not use for the final website.

Again by clicking on each of these small pictures another page appears showing the item in a similar designed web page.

And if appropriate there should be an option to choose between different color versions of the same set, which can go in maximum three different colors.

On each of the collection page there should be a rectangular frame, which looks like a jewellery box (see the picture for the style of the box we have chosen), with a further option to go to next pages in each corner. The name of each collection should be clearly written in the page.

The keywords for the buttons will be:
Origin
Buy
Ask
Become a fan

The “Origin” page will explain the background and history of the artist and the cultural heritage is refers to. This page has also to be designed in the same style as the other pages, but will read like a story in book which can contain different chapters:
- artist interview
- design origin
- cultural heritage
- preferred usage and tips
- etc.

The “Buy” page will provide the necessary elements to order the item. For this we will use a module of FenTorWabble. The only thing needed for this page from a point of design is the background.

The “Ask” page will be on the possibility to send us an e-mail with questions. It will contain some items to be selected, but again for this page from a point of design the only thing needed for this page is the background.

The “Become a fan” page will contain the possibility to register yourself as a fan to get regular newsletters and updates by e-mail from VPK.

We like the following examples of other jewelery websites
www.quiv-gemhouse.example
www.pelmorstones.example

The final result we will need are layered PSD files.
Updates

We have discussed in our team the technicalities of what we actually need in this contest.

What we will need is "Uncoded" files.
Outside this contest we will ask a web developer/designer to code it and to bring it into a working web page.

We have updated our brief accordingly.

Target Market(s)

Industry/Entity Type

It Company

Requirements
Must have
• The website should be really creative and be of another nature than informative websites. It should be a pleasure and a kind of discovery to go through our website.
Nice to have
• If the web site has moving elements, than it should drag you in from one page to another, like you are opening boxes.
Should not have
• The idea is that the website is not going crazy with pop ups and moving things, but is distinguished and a pleasure to look at.

```html
<!DOCTYPE html>
<html lang="en">
<head>
<meta charset="utf-8">
<title>Vorandine Pesa Kolun – Collection</title>
<link href="https://fonts.googleapis.com/css2?family=Didact+Gothic&family=PT+Sans:wght@700&family=Pinyon+Script&display=swap" rel="stylesheet">
<style>
  :root {
    --page-bg: #000000;
    --rule: #8c8c8c;
    --nav-text: #f2f2f2;
    --brand-silver: #b8b8b8;
    --panel-light: #b3b3b3;
    --panel-shade: #7d7d7d;
    --panel-text: #1a1a1a;
    --script-grey: #8a8a8a;
    --thumb-border: #9a9a9a;
    --arrow: #a8a8a8;
    --footer-text: #e6e6e6;
  }
  * { margin: 0; padding: 0; box-sizing: border-box; }
  html, body { width: 1200px; height: 703px; overflow: hidden; background: var(--page-bg); }
  .page { position: relative; width: 1200px; height: 703px; font-family: "Didact Gothic", sans-serif; }

  .rule { position: absolute; height: 1px;
    background: linear-gradient(90deg, rgba(140,140,140,0.5), var(--rule) 30%, #d0d0d0 50%, var(--rule) 70%, rgba(140,140,140,0.5)); }
  .rule--top { left: 62px; width: 1076px; top: 103px; }
  .rule--bottom { left: 62px; width: 1076px; top: 570px; }

  .brand { position: absolute; left: 520px; top: 17px; width: 160px; height: 133px; background: var(--page-bg);
    display: flex; flex-direction: column; align-items: center; justify-content: flex-end; gap: 6px; }
  .brand__name { font-size: 44px; color: var(--brand-silver); letter-spacing: 2px; line-height: 1; }
  .brand__sub { font-size: 12px; color: var(--brand-silver); border-top: 1px solid var(--brand-silver); padding-top: 3px; width: 100px; text-align: center; }

  .nav a { position: absolute; top: 134px; font-family: "PT Sans", sans-serif; font-weight: 700; font-size: 15px;
    color: var(--nav-text); text-decoration: none; letter-spacing: 0; }
  .nav .is-current { color: #ffffff; }

  .showcase { position: absolute; left: 180px; top: 180px; width: 458px; height: 345px;
    background: radial-gradient(ellipse at 70% 40%, #1f4f57 0%, #0d2226 30%, #050708 65%, #000 100%); }
  .showcase__second { position: absolute; left: 30px; top: 120px; width: 170px; height: 140px;
    background: radial-gradient(ellipse, #24717c 0%, #0b2a2f 55%, transparent 75%); }

  .thumbs { position: absolute; top: 451px; }
  .thumb { position: absolute; top: 0; width: 54px; height: 54px; border: 1px solid var(--thumb-border); }
  .thumb--teal { background: radial-gradient(circle, #2a7f88, #0b2326 75%); }
  .thumb--clear { background: radial-gradient(circle, #8c8f99, #141416 75%); }
  .thumb--pink { background: radial-gradient(circle, #8a6a86, #141014 75%); }

  .arrow { position: absolute; top: 466px; }

  .info { position: absolute; left: 638px; top: 180px; width: 385px; height: 345px; background: var(--panel-light); }
  .info__shade { position: absolute; left: 0; top: 0; width: 91px; height: 345px;
    background: linear-gradient(180deg, var(--panel-shade), #6f7476 40%, #5f7b80 55%, var(--panel-shade) 80%); }
  .info__kicker { position: absolute; right: 22px; top: 8px; font-family: "Pinyon Script", cursive;
    font-size: 42px; color: var(--script-grey); line-height: 1.1; }
  .info__title { position: absolute; left: 114px; top: 72px; font-weight: 400; font-size: 18px; color: var(--panel-text); }
  .info__text { position: absolute; left: 114px; top: 119px; width: 250px; font-size: 14px; line-height: 22.5px; color: var(--panel-text); }

  .ornament-band { position: absolute; left: 272px; top: 525px; width: 646px; height: 37px;
    background: linear-gradient(90deg, transparent, rgba(90,90,90,0.45) 25%, rgba(110,110,110,0.5) 50%, rgba(90,90,90,0.45) 75%, transparent); }
  .ornament-center { position: absolute; left: 565px; top: 556px; width: 60px; height: 30px; background: var(--page-bg);
    border-radius: 50%; box-shadow: inset 0 0 0 1px #7a7a7a; }

  .footer { position: absolute; left: 0; width: 1200px; top: 606px; text-align: center;
    font-size: 14px; line-height: 22.5px; color: var(--footer-text); }
</style>
</head>
<body>
<div class="page">
  <div class="rule rule--top"></div>

  <div class="brand">
    <span class="brand__name">VPK</span>
    <span class="brand__sub">Vorandine</span>
  </div>

  <nav class="nav">
    <a class="is-current" href="#" style="left:207px">COLLECTION</a>
    <a href="#" style="left:316px">ORIGIN</a>
    <a href="#" style="left:388px">BUY</a>
    <a href="#" style="left:857px">ASK</a>
    <a href="#" style="left:909px">BECOME A FAN</a>
  </nav>

  <div class="showcase" role="img" aria-label="Photograph of a teal crystal beaded ring and bracelet on a black reflective surface">
    <div class="showcase__second"></div>
  </div>

  <svg class="arrow" style="left:225px" width="20" height="24" viewBox="0 0 20 24" aria-hidden="true">
    <polygon points="16,2 4,12 16,22 12,12" fill="var(--arrow)"/>
  </svg>
  <div class="thumbs">
    <div class="thumb thumb--teal" style="left:272px" role="img" aria-label="Thumbnail of the teal ring"></div>
    <div class="thumb thumb--clear" style="left:345px" role="img" aria-label="Thumbnail of a crystal necklace"></div>
    <div class="thumb thumb--pink" style="left:417px" role="img" aria-label="Thumbnail of a pink bow pendant"></div>
    <div class="thumb thumb--pink" style="left:490px" role="img" aria-label="Thumbnail of a pink butterfly pendant"></div>
  </div>
  <svg class="arrow" style="left:572px" width="20" height="24" viewBox="0 0 20 24" aria-hidden="true">
    <polygon points="4,2 16,12 4,22 8,12" fill="var(--arrow)"/>
  </svg>

  <section class="info">
    <div class="info__shade" role="img" aria-label="Faded edge of the jewellery photograph"></div>
    <div class="info__kicker">Complete Set</div>
    <h1 class="info__title">Lagoon Veil</h1>
    <p class="info__text">Fine silver thread has been shaped into slender loops and playfully adorned with clusters of mixed glass beads and deep tones of ocean teal. Full size is 75mm.</p>
  </section>

  <div class="ornament-band" role="img" aria-label="Baroque lace pattern band"></div>
  <div class="rule rule--bottom"></div>
  <div class="ornament-center" role="img" aria-label="Baroque scroll ornament"></div>

  <footer class="footer">
    <p>Copyright (c) www.vorandine-shop.example 2011</p>
    <p>Allright reserved</p>
  </footer>
</div>
</body>
</html>
```